Kestrel Lane Medical

Stationary design including letterhead A4, appointment card and with compliments
Updates

Hi Designers, we have some orange boxes in and around our main cross, we would like to see if those boxes could be used s part of the stationary design. Perhaps bouncing along the bottom of the page. Cheers Dot

Target Market(s)

We are a general practice with a wide range of patients.

Industry/Entity Type

Medical

Font styles to use
Serif
Sans Serif

Colors
9ccb3b
f37022
a64599

Requirements
Must have
• Address and contact details
Logo.Address
Shop 4, 19 Pellow Road, TARLEE SA 5412
Phone 08 84617352
Fax 08 84617390
web site - www.kestrellanemedical.com.au
Nice to have
• We have small boxes in our logo we would like used as a design element of the stationary.
Should not have
• Hard to read, script.

```html
<!DOCTYPE html>
<html lang="en">
<head>
<meta charset="utf-8">
<title>Kestrel Lane Medical – Stationery</title>
<link rel="stylesheet" href="https://fonts.googleapis.com/css2?family=Open+Sans:wght@400;600;700&display=swap">
<style>
  :root {
    --purple: #7a1472;
    --purple-soft: #a64599;
    --green: #9ccb3b;
    --orange: #f37022;
    --ink: #3a3a3a;
    --muted: #777;
    --paper: #ffffff;
    --backdrop: #ededed;
    --rule: #c9c9c9;
  }
  * { box-sizing: border-box; margin: 0; padding: 0; }
  html, body { width: 1200px; height: 795px; overflow: hidden; }
  body {
    position: relative;
    background: var(--backdrop);
    font-family: "Open Sans", sans-serif;
    color: var(--ink);
  }
  .sheet {
    position: absolute;
    background: var(--paper);
    box-shadow: 0 2px 8px rgba(0,0,0,.12);
    overflow: hidden;
  }
  .brand { display: flex; align-items: center; gap: 8px; }
  .brand-dot {
    flex: none; border-radius: 50%;
    background: var(--green);
  }
  .brand-name {
    font-weight: 700; color: var(--purple);
    text-transform: uppercase; line-height: 1.05; letter-spacing: .02em;
  }
  .contact { font-size: 7px; line-height: 1.45; color: var(--ink); }
  .contact dl { display: grid; grid-template-columns: auto auto; column-gap: 6px; justify-content: start; }
  .contact dt { color: var(--purple); font-weight: 700; }
  .contact .web { color: var(--purple); font-weight: 700; }
  .band { position: absolute; left: 0; right: 0; background: var(--purple); }
  .cross-art {
    position: absolute;
    background: radial-gradient(circle at 40% 45%, rgba(156,203,59,.55), rgba(156,203,59,.25) 55%, rgba(243,112,34,.12) 75%, rgba(255,255,255,0) 100%);
  }

  /* Letterhead */
  .letterhead { left: 40px; top: 40px; width: 500px; height: 707px; }
  .letterhead .brand { position: absolute; left: 44px; top: 44px; }
  .letterhead .brand-dot { width: 26px; height: 26px; }
  .letterhead .brand-name { font-size: 14px; }
  .letterhead .contact { position: absolute; right: 44px; top: 44px; font-size: 8px; }
  .letter-body { position: absolute; left: 44px; top: 150px; width: 330px; font-size: 9px; line-height: 1.65; }
  .letter-body p { margin-bottom: 10px; }
  .letter-body .salutation { font-weight: 700; }
  .signature { position: absolute; left: 44px; top: 470px; }
  .signature .sign-name { font-size: 16px; color: var(--ink); }
  .signature .sign-role { font-size: 8px; font-weight: 700; margin-top: 2px; }
  .letterhead .cross-art { right: 20px; bottom: 70px; width: 170px; height: 150px; }
  .letterhead .band { bottom: 44px; height: 7px; }

  /* Compliments slip */
  .slip { left: 590px; top: 40px; width: 570px; height: 266px; }
  .slip .contact { position: absolute; left: 300px; top: 30px; }
  .slip .cross-art { right: 18px; top: 20px; width: 120px; height: 110px; }
  .slip .brand { position: absolute; left: 30px; top: 150px; }
  .slip .brand-dot { width: 20px; height: 20px; }
  .slip .brand-name { font-size: 11px; }
  .slip .slip-title { position: absolute; left: 30px; bottom: 36px; font-size: 20px; color: var(--purple); }
  .slip .band { bottom: 20px; height: 6px; }

  /* Business card */
  .card { left: 590px; width: 270px; height: 158px; }
  .business-card { top: 336px; }
  .business-card .brand { position: absolute; left: 16px; top: 74px; }
  .business-card .brand-dot { width: 18px; height: 18px; }
  .business-card .brand-name { font-size: 9px; }
  .business-card .contact { position: absolute; left: 140px; top: 18px; font-size: 6.5px; }
  .card .band { bottom: 20px; height: 5px; }

  /* Appointment card */
  .appointment-card { top: 516px; }
  .appointment-card .cross-art { right: 8px; top: 6px; width: 80px; height: 70px; }
  .appt-lines { position: absolute; left: 18px; top: 28px; width: 170px; list-style: none; font-size: 7px; color: var(--muted); }
  .appt-lines li { display: flex; gap: 6px; align-items: flex-end; height: 20px; }
  .appt-lines li span { width: 26px; }
  .appt-lines li::after { content: ""; flex: 1; border-bottom: 1px solid var(--rule); margin-bottom: 2px; }

  /* Notebook */
  .notebook { left: 890px; top: 336px; width: 270px; height: 411px; }
  .notebook .spiral { position: absolute; left: 6px; top: 14px; bottom: 14px; width: 10px; }
  .notebook .brand { position: absolute; left: 50%; top: 120px; transform: translateX(-50%); flex-direction: column; text-align: center; gap: 8px; }
  .notebook .brand-dot { width: 34px; height: 34px; }
  .notebook .brand-name { font-size: 15px; }
</style>
</head>
<body>

<section class="sheet letterhead" aria-label="Letterhead">
  <div class="brand"><span class="brand-dot"></span><span class="brand-name">Kestrel Lane<br>Medical</span></div>
  <address class="contact">
    <dl><dt>PHONE</dt><dd>08 84617352</dd><dt>FAX</dt><dd>08 84617390</dd></dl>
    <div>Shop 4, 19 Pellow Road,<br>TARLEE SA 5412</div>
    <div class="web">www.kestrellanemedical.com.au</div>
  </address>
  <div class="letter-body">
    <p class="salutation">Dear Patient,</p>
    <p>Thank you for choosing our practice for your family's health care. Our doctors and nurses are here to help you stay well throughout the year.</p>
    <p>Appointments can be booked by phone or in person at reception. Please arrive ten minutes early and bring your health card with you.</p>
    <p>We offer general check-ups, vaccinations, health plans and care for chronic conditions for patients of every age.</p>
    <p>If you have any questions about your care, please speak with our friendly team. We look forward to seeing you soon.</p>
  </div>
  <div class="signature">
    <div class="sign-name">Your Name</div>
    <div class="sign-role">Company Director</div>
  </div>
  <div class="cross-art" role="img" aria-label="Faint green medical cross with small orange boxes"></div>
  <div class="band"></div>
</section>

<section class="sheet slip" aria-label="With compliments slip">
  <address class="contact">
    <dl><dt>PHONE</dt><dd>08 84617352</dd><dt>FAX</dt><dd>08 84617390</dd></dl>
    <div>Shop 4, 19 Pellow Road,<br>TARLEE SA 5412</div>
    <div class="web">www.kestrellanemedical.com.au</div>
  </address>
  <div class="cross-art" role="img" aria-label="Faint green medical cross with small orange boxes"></div>
  <div class="brand"><span class="brand-dot"></span><span class="brand-name">Kestrel Lane<br>Medical</span></div>
  <div class="slip-title">With compliments</div>
  <div class="band"></div>
</section>

<section class="sheet card business-card" aria-label="Business card">
  <address class="contact">
    <dl><dt>PHONE</dt><dd>08 84617352</dd><dt>FAX</dt><dd>08 84617390</dd></dl>
    <div>Shop 4, 19 Pellow Road,<br>TARLEE SA 5412</div>
    <div class="web">www.kestrellanemedical.com.au</div>
  </address>
  <div class="brand"><span class="brand-dot"></span><span class="brand-name">Kestrel Lane<br>Medical</span></div>
  <div class="band"></div>
</section>

<section class="sheet card appointment-card" aria-label="Appointment card">
  <ul class="appt-lines">
    <li><span>Name</span></li>
    <li><span>Date</span></li>
    <li><span>Time</span></li>
    <li><span>With</span></li>
  </ul>
  <div class="cross-art" role="img" aria-label="Faint green medical cross with small orange boxes"></div>
  <div class="band"></div>
</section>

<section class="sheet notebook" aria-label="Notebook cover">
  <svg class="spiral" viewBox="0 0 10 383" preserveAspectRatio="none" aria-hidden="true">
    <g fill="none" stroke="#555" stroke-width="1.5">
      <circle cx="5" cy="8" r="3"/><circle cx="5" cy="26" r="3"/><circle cx="5" cy="44" r="3"/><circle cx="5" cy="62" r="3"/>
      <circle cx="5" cy="80" r="3"/><circle cx="5" cy="98" r="3"/><circle cx="5" cy="116" r="3"/><circle cx="5" cy="134" r="3"/>
      <circle cx="5" cy="152" r="3"/><circle cx="5" cy="170" r="3"/><circle cx="5" cy="188" r="3"/><circle cx="5" cy="206" r="3"/>
      <circle cx="5" cy="224" r="3"/><circle cx="5" cy="242" r="3"/><circle cx="5" cy="260" r="3"/><circle cx="5" cy="278" r="3"/>
      <circle cx="5" cy="296" r="3"/><circle cx="5" cy="314" r="3"/><circle cx="5" cy="332" r="3"/><circle cx="5" cy="350" r="3"/>
      <circle cx="5" cy="368" r="3"/>
    </g>
  </svg>
  <div class="brand"><span class="brand-dot"></span><span class="brand-name">Kestrel Lane<br>Medical</span></div>
</section>

</body>
</html>
```